Business Card Design Project

Im an electrician and my company name is Kestrel Electrical
My main work is installing Lighting and Power Points, Home Theater Systems, TVS, Phones and Data
Im looking a business card, something nice, clean, modern and not to cluttered
Im open to sugestions
I dont mind if the "Services" is on the back on the business card
colours black, grey, white or the blue colour of my logo are prefered but not compulsory
any questions just message me
and please make it so if i need to edit the writing can do it easy. maybe by making it a seperate layer ?
My Details are.
Name - Peter Halloran
Job Title - Licenced Electrician
Mobile - 027 583 2174
Email - peter@kestrelelectrical.co.nz
Web - www.kestrelelectrical.co.nz
Services
Residential / Commercial
Lighting & Power
Heating & Ventilation
Automation
Phone & Data
Home Cinema
Sound Systems
TV, Antenna & Satellite
Digital Upgrades

```html
<!DOCTYPE html>
<html lang="en">
<head>
<meta charset="utf-8">
<title>Kestrel Electrical – Business Cards</title>
<link rel="stylesheet" href="https://fonts.googleapis.com/css2?family=Roboto+Condensed:wght@400;700&family=Varela+Round&family=Open+Sans:wght@400&display=swap">
<style>
  :root {
    --brand-blue: #12b4cf;
    --brand-grey: #6b6d72;
    --ink: #333538;
    --paper: #ffffff;
    --backdrop: #7b4e31;
    --label: #1e1a17;
  }
  * { box-sizing: border-box; margin: 0; padding: 0; }
  html, body { width: 1200px; height: 788px; overflow: hidden; }
  body { background: var(--backdrop); position: relative; font-family: "Roboto Condensed", sans-serif; color: var(--ink); }

  .sheet-label {
    position: absolute; width: 525px; text-align: center;
    font-family: "Open Sans", sans-serif; font-size: 22px; color: var(--label);
  }

  .card {
    position: absolute; width: 525px; height: 300px;
    background: var(--paper); border-radius: 22px; overflow: hidden;
  }
  .card--blue { background: var(--brand-blue); color: var(--paper); }

  .wordmark {
    position: absolute; display: flex; align-items: center; gap: 14px;
    font-family: "Roboto Condensed", sans-serif; font-weight: 700;
    color: var(--brand-blue); text-transform: uppercase; line-height: 1.02;
  }
  .wordmark__square { width: 22px; height: 22px; background: var(--brand-blue); flex: none; }
  .card--blue .wordmark { color: var(--paper); }
  .card--blue .wordmark__square { background: var(--paper); }

  /* Front */
  .corner-swoosh { position: absolute; }
  .holder { position: absolute; right: 279px; top: 194px; text-align: right; font-family: "Varela Round", sans-serif; }
  .holder__name { color: var(--brand-blue); font-size: 18px; }
  .holder__title { color: var(--brand-grey); font-size: 13px; margin-top: 4px; }
  .divider { position: absolute; width: 1px; background: #8a8c90; }
  .contact { position: absolute; left: 274px; top: 180px; list-style: none; font-size: 13.5px; line-height: 24px; }
  .contact b { font-weight: 700; }

  /* Services */
  .services-title { position: absolute; color: var(--brand-blue); font-weight: 700; font-size: 18px; }
  .card--blue .services-title { color: var(--paper); }
  .services-inline { position: absolute; left: 0; width: 100%; top: 180px; text-align: center; font-size: 15.5px; line-height: 24.3px; }
  .services-inline span::before, .services-list li::before { content: "▪"; margin-right: 6px; font-size: 11px; vertical-align: 2px; }
  .services-list { position: absolute; list-style: none; font-size: 16px; line-height: 24.2px; }
  .card--blue .services-list { font-size: 15.5px; line-height: 20px; }
  .services-list li.continued::before { visibility: hidden; }
</style>
</head>
<body>

  <p class="sheet-label" style="left:54px; top:32px;">Front</p>
  <p class="sheet-label" style="left:622px; top:32px;">Back - 1</p>
  <p class="sheet-label" style="left:54px; top:403px;">Back - 2</p>
  <p class="sheet-label" style="left:622px; top:403px;">Back - 3</p>

  <!-- Front -->
  <section class="card" style="left:54px; top:74px;">
    <svg class="corner-swoosh" style="right:0; top:0;" width="90" height="40" viewBox="0 0 90 40" aria-hidden="true">
      <path d="M0 0 Q60 2 90 34 L90 22 Q70 4 30 0 Z" fill="var(--brand-grey)"/>
      <path d="M10 0 Q66 0 90 22 L90 0 Z" fill="var(--brand-blue)"/>
    </svg>
    <svg class="corner-swoosh" style="left:0; bottom:0;" width="90" height="40" viewBox="0 0 90 40" aria-hidden="true">
      <path d="M0 6 Q30 28 80 40 L60 40 Q20 30 0 16 Z" fill="var(--brand-grey)"/>
      <path d="M0 16 Q24 34 70 40 L0 40 Z" fill="var(--brand-blue)"/>
    </svg>

    <div class="wordmark" style="left:104px; top:58px; font-size:38px;">
      <span class="wordmark__square"></span>
      <span>Kestrel<br>Electrical</span>
    </div>

    <div class="holder">
      <p class="holder__name">Peter Halloran</p>
      <p class="holder__title">Licenced Electrician</p>
    </div>
    <span class="divider" style="left:262px; top:182px; height:64px;"></span>
    <ul class="contact">
      <li><b>cell</b> 027 583 2174</li>
      <li><b>email</b> peter@kestrelelectrical.co.nz</li>
      <li><b>web</b> www.kestrelelectrical.co.nz</li>
    </ul>
  </section>

  <!-- Back 1 -->
  <section class="card" style="left:622px; top:74px;">
    <div class="wordmark" style="left:120px; top:42px; font-size:40px;">
      <span class="wordmark__square"></span>
      <span>Kestrel<br>Electrical</span>
    </div>
    <h2 class="services-title" style="left:0; width:100%; text-align:center; top:156px;">SERVICES</h2>
    <p class="services-inline">
      <span>Residential / Commercial</span> <span>Lighting &amp; Power</span><br>
      <span>Heating &amp; Ventilation</span> <span>Automation</span> <span>Phone &amp; Data</span><br>
      <span>Home Cinema</span> <span>Sound Systems</span><br>
      <span>TV, Antenna &amp; Satellite</span> <span>Digital Upgrades</span>
    </p>
  </section>

  <!-- Back 2 -->
  <section class="card" style="left:54px; top:445px;">
    <div class="wordmark" style="left:40px; top:114px; font-size:30px;">
      <span class="wordmark__square" style="width:16px; height:16px;"></span>
      <span>Kestrel<br>Electrical</span>
    </div>
    <span class="divider" style="left:259px; top:28px; height:243px;"></span>
    <h2 class="services-title" style="left:282px; top:24px; font-size:22px;">SERVICES</h2>
    <ul class="services-list" style="left:278px; top:59px;">
      <li>Residential / Commercial</li>
      <li>Lighting &amp; Power</li>
      <li>Heating &amp; Ventilation</li>
      <li>Automation</li>
      <li>Phone &amp; Data</li>
      <li>Home Cinema</li>
      <li>Sound Systems</li>
      <li>TV, Antenna &amp; Satellite</li>
      <li>Digital Upgrades</li>
    </ul>
  </section>

  <!-- Back 3 -->
  <section class="card card--blue" style="left:622px; top:445px;">
    <div class="wordmark" style="left:140px; top:32px; font-size:34px;">
      <span class="wordmark__square"></span>
      <span>Kestrel<br>Electrical</span>
    </div>
    <h2 class="services-title" style="left:0; width:100%; text-align:center; top:152px;">SERVICES</h2>
    <ul class="services-list" style="left:92px; top:183px;">
      <li>Residential</li>
      <li class="continued">Commercial</li>
      <li>Lighting &amp; Power</li>
      <li>Heating &amp; Ventilation</li>
      <li>Automation</li>
    </ul>
    <ul class="services-list" style="left:262px; top:183px;">
      <li>Phone &amp; Data</li>
      <li>Home Cinema</li>
      <li>Sound Systems</li>
      <li>TV, Antenna &amp; Satellite</li>
      <li>Digital Upgrades</li>
    </ul>
  </section>

</body>
</html>
```